need a business card designed, I work with independent car dealerships throughout the US, I connect them with Buyers ( private investors, banks, credit unions, finance co's etc... ) that want to purchase their loan portfolio's, also consult on cashflow management, business lines of credit etc... looking for a consultant look, but something that attracts small business owners
Pellardi Consulting

Business

```html
<!DOCTYPE html>
<html lang="en">
<head>
<meta charset="utf-8">
<title>Pellardi Consulting – Business Card</title>
<link rel="stylesheet" href="https://fonts.googleapis.com/css2?family=Ubuntu:wght@500&family=PT+Sans:wght@400&display=swap">
<style>
  :root {
    --page-bg: #e4e4e4;
    --card-red: #ec1c24;
    --card-blue: #1757a4;
    --band-white: #ffffff;
    --name-blue: #1a56a0;
    --contact-white: #ffffff;
  }
  * { margin: 0; padding: 0; box-sizing: border-box; }
  html, body {
    width: 1200px;
    height: 900px;
    overflow: hidden;
    background: var(--page-bg);
  }
  .canvas {
    position: relative;
    width: 1200px;
    height: 900px;
  }
  .business-card {
    position: absolute;
    left: 80px;
    top: 150px;
    width: 1040px;
    height: 600px;
    display: flex;
    box-shadow: 0 6px 24px rgba(0, 0, 0, 0.18);
  }
  .card-front-panel {
    position: relative;
    width: 570px;
    height: 100%;
    background: var(--card-red);
  }
  .card-contact-panel {
    position: relative;
    flex: 1;
    height: 100%;
    background: var(--card-blue);
  }
  .name-band {
    position: absolute;
    left: 0;
    top: 160px;
    width: 570px;
    height: 104px;
    background: var(--band-white);
    font-family: "Ubuntu", sans-serif;
    font-weight: 500;
    color: var(--name-blue);
    text-align: center;
    padding-top: 8px;
  }
  .person-name {
    font-size: 46px;
    line-height: 52px;
    padding-left: 30px;
  }
  .company-name {
    font-size: 34px;
    line-height: 40px;
    padding-left: 40px;
  }
  .contact-list {
    position: absolute;
    left: 32px;
    top: 420px;
    font-family: "PT Sans", sans-serif;
    font-size: 26px;
    color: var(--contact-white);
    list-style: none;
  }
  .contact-item {
    display: flex;
    height: 50px;
    align-items: center;
  }
  .contact-label { width: 88px; }
  .contact-sep { width: 28px; }
</style>
</head>
<body>
  <main class="canvas">
    <article class="business-card">
      <section class="card-front-panel">
        <div class="name-band">
          <h1 class="person-name">Daniel R Pellardi</h1>
          <h2 class="company-name">Pellardi Consulting</h2>
        </div>
      </section>
      <section class="card-contact-panel">
        <ul class="contact-list">
          <li class="contact-item"><span class="contact-label">Tel</span><span class="contact-sep">:</span><span class="contact-value">555-214-6083</span></li>
          <li class="contact-item"><span class="contact-label">Fax</span><span class="contact-sep">:</span><span class="contact-value">555-730-4418</span></li>
          <li class="contact-item"><span class="contact-label">E-mail</span><span class="contact-sep">:</span><span class="contact-value">lenderlink4@mailbox.com</span></li>
        </ul>
      </section>
    </article>
  </main>
</body>
</html>
```